"Harlow's True Grain Woodwork" with a logo of a saw blade and handplane combined

Need a business card logo with a saw blade and hand plane
combined with Harlow's True Grain Woodwork on it, and a unique design.

Woodworking has been in my family for generations, from carpentry, to milling logs for old farm homes and barns in the 1930's and 1940's. My grandfather had a small carpentry business from his home,and passed his skills down to my father who also did woodworking from his own small business. Having the passion for woodwork in my blood, I'm trying to continue with my own small business doing custom fine woodwork such as tables, small cabinetry and even outdoor projects to suite the customers needs. All my projects start with a rough piece of lumber, what ever the species suited for the project, and is milled to dimensions , assembled, and finished all by hand for a true handcrafted project.

My target market would be people who want a custom handmade piece, something that they can't find in stores and is unique. Also people who are willing to pay and appreciate the value, which is sometimes a hard market to find.

As far as design, I think I would like to get a sleek looking saw blade on the card combined with a hand plane some how. Background colour maybe a dark wood texture or grey? Colours I like are grey, black, reds, white, yellows but depending on how the card is looking I'm not afraid to use a cool colour to make something stand out. Just want the card to flow ,look clean and unique. Lettering I like serif and script or something similar to these that looks good on the card.

Facebook page is under Harlow's True Grain Woodwork
Updates

If I could get logo on the card, a saw blade, hand plane or combine both together would be nice! Added Saturday, June 11, 2016

Target Market(s)

People that like a unique hand made project built to last

Industry/Entity Type

Business

Contact Information for Business Card

Harlows True Grain Woodwork
Hand crafted by: Owen Harlow
Phone: 555 718-2265
Address: 412 Birchmont Rd. Wrenfield-On-The-Shore
Email: harlowstruegrain@mailpost.example
Facebook: Harlows True Grain Woodwork
prefer icons for the info!

Font styles to use
Serif
Script

Requirements
Must have
• Nice clean look, little bit bold with an elegant taste
• Prefer black lettering
Nice to have
• I like silver for the saw blade and silver with brown handles on the hand plane!
Should not have
• Bright colours

```html
<!DOCTYPE html>
<html lang="en">
<head>
<meta charset="utf-8">
<title>Harlow's True Grain Woodwork — Business Card</title>
<link rel="stylesheet" href="https://fonts.googleapis.com/css2?family=Questrial&display=swap">
<style>
  :root {
    --stage: #2e2b29;
    --card-black: #1b1a1a;
    --wood-light: #d9a26a;
    --wood-mid: #c2874f;
    --wood-dark: #9c6535;
    --engrave: #6e3a1c;
    --text-grey: #c9c9c9;
    --copper: #8a4a2a;
    --silver: #bfc1c3;
    --panel: #000000;
  }
  * { margin: 0; padding: 0; box-sizing: border-box; }
  html, body { width: 1200px; height: 727px; overflow: hidden; }
  body {
    background: var(--stage);
    font-family: "Questrial", "Century Gothic", sans-serif;
    position: relative;
  }

  .card {
    position: absolute;
    width: 525px;
    height: 300px;
    border-radius: 3px;
    overflow: hidden;
    box-shadow: 0 10px 30px rgba(0,0,0,.45);
  }

  /* Front: wood surface with engraved name */
  .card--front { left: 40px; top: 40px; }
  .wood-surface {
    position: absolute; inset: 0;
    background: linear-gradient(100deg, var(--wood-light) 0%, var(--wood-mid) 45%, var(--wood-light) 70%, var(--wood-dark) 100%);
  }
  .front-mark {
    position: absolute; left: 0; right: 0; top: 92px;
    text-align: center; color: var(--engrave);
  }
  .front-mark .mark-name { font-size: 64px; line-height: 1; letter-spacing: 1px; }
  .front-mark .mark-tag { font-size: 25px; letter-spacing: 2px; margin-top: 8px; }

  /* Back: contact side */
  .card--back {
    left: 625px; top: 195px;
    background: var(--card-black);
  }
  .contact {
    position: absolute; left: 30px; top: 38px;
    color: var(--text-grey);
  }
  .contact .credit { color: var(--copper); font-size: 13px; letter-spacing: .5px; }
  .contact .owner { font-size: 25px; margin: 2px 0 14px; }
  .contact-list { list-style: none; font-size: 13px; line-height: 22px; }
  .contact-list li { display: flex; align-items: center; gap: 9px; white-space: nowrap; }
  .contact-list svg { width: 12px; height: 12px; flex: none; fill: var(--copper); }

  .back-mark {
    position: absolute; right: 28px; bottom: 40px;
    text-align: right; color: var(--text-grey);
  }
  .back-mark .mark-name { font-size: 40px; line-height: 1; }
  .back-mark .mark-tag { font-size: 16px; letter-spacing: 1.5px; margin-top: 6px; }

  /* Standalone logo panel */
  .logo-panel {
    position: absolute; left: 0; bottom: 0;
    width: 420px; height: 215px;
    background: var(--panel);
    color: var(--silver);
    display: flex; flex-direction: column; align-items: center; justify-content: center;
  }
  .logo-panel .mark-row { display: flex; align-items: center; gap: 14px; }
  .logo-panel .mark-dot { width: 22px; height: 22px; border-radius: 50%; background: var(--silver); }
  .logo-panel .mark-name { font-size: 56px; line-height: 1; }
  .logo-panel .mark-tag { font-size: 24px; letter-spacing: 2px; margin-top: 14px; }
</style>
</head>
<body>

  <section class="card card--front">
    <div class="wood-surface" role="img" aria-label="Warm honey-toned wood grain texture"></div>
    <div class="front-mark">
      <div class="mark-name">Harlows</div>
      <div class="mark-tag">True Grain Woodwork</div>
    </div>
  </section>

  <section class="card card--back">
    <div class="contact">
      <p class="credit">Hand crafted by</p>
      <p class="owner">Owen Harlow</p>
      <ul class="contact-list">
        <li>
          <svg viewBox="0 0 12 12" aria-hidden="true"><path d="M2.5 1h2l1 3-1.5 1a7 7 0 0 0 3 3l1-1.5 3 1v2c0 .6-.4 1-1 1A10 10 0 0 1 1 2c0-.6.4-1 1-1z"/></svg>
          555 718-2265
        </li>
        <li>
          <svg viewBox="0 0 12 12" aria-hidden="true"><path d="M6 0a4 4 0 0 1 4 4c0 3-4 8-4 8S2 7 2 4a4 4 0 0 1 4-4zm0 2.3a1.7 1.7 0 1 0 0 3.4 1.7 1.7 0 0 0 0-3.4z"/></svg>
          412 Birchmont Rd. Wrenfield-On-The-Shore
        </li>
        <li>
          <svg viewBox="0 0 12 12" aria-hidden="true"><path d="M0 2h12v8H0zM1 3l5 4 5-4"/></svg>
          harlowstruegrain@mailpost.example
        </li>
        <li>
          <svg viewBox="0 0 12 12" aria-hidden="true"><rect x="0" y="0" width="12" height="12" rx="1.5"/></svg>
          Harlows True Grain Woodwork
        </li>
      </ul>
    </div>
    <div class="back-mark">
      <div class="mark-name">Harlows</div>
      <div class="mark-tag">True Grain Woodwork</div>
    </div>
  </section>

  <section class="logo-panel">
    <div class="mark-row">
      <span class="mark-dot"></span>
      <span class="mark-name">Harlows</span>
    </div>
    <div class="mark-tag">True Grain Woodwork</div>
  </section>

</body>
</html>
```